Simple elegant feminine design - Going out on my own as a Mortgage Broker.
My thoughts are the following details on the Front, middle of the card possibly? Phone and email smaller font than my name?
Marnie Veltrin
Finance Specialist
p: 0438 215 962
e: marnie@veltrinlending.com.au
Bottom of the card
residential / commercial / equipment
I would like the Font in Rose Gold maybe white or black background? or Possibly a stone grey - are you able to do a few options? I'd like them embossed
Then I had an idea as a simple logo as per the attached if you get the idea in my scribble, my initials, capital M attached to a small v that leads/follows into a circle? Thicker Font In Rose Gold, middle of the card at the back.
Very open to ideas though and what colour you think would look better with the Rose Gold.
Thanks so much for your help, I am not very creative and savvy with this stuff :-)
Industry/Entity Type
Finance
Contact Information for Business Card
Marnie Veltrin
p: 0438 215 962
Look and feel

```html
<!DOCTYPE html>
<html lang="en">
<head>
<meta charset="utf-8">
<title>Marnie's Business Cards</title>
<link rel="stylesheet" href="https://fonts.googleapis.com/css2?family=Arimo:ital,wght@1,400&display=swap">
<style>
  :root {
    --page: #ffffff;
    --card: #ffffff;
    --card-edge: #e6e6e6;
    --ink: #111111;
    --rose: #8c5560;
  }
  html, body {
    margin: 0;
    padding: 0;
    width: 1200px;
    height: 1200px;
    overflow: hidden;
    background: var(--page);
  }
  .card {
    position: absolute;
    left: 150px;
    top: 254px;
    width: 978px;
    height: 582px;
    background: var(--card);
    border: 1px solid var(--card-edge);
    box-sizing: border-box;
    font-family: "Arimo", Arial, sans-serif;
    font-style: italic;
  }
  .brand {
    position: absolute;
    left: 78px;
    top: 92px;
    display: flex;
    align-items: center;
    gap: 12px;
    color: var(--rose);
    font-size: 24px;
    line-height: 1;
  }
  .brand-dot {
    width: 34px;
    height: 34px;
    border: 3px solid var(--rose);
    border-radius: 50%;
    box-sizing: border-box;
  }
  .details {
    position: absolute;
    left: 490px;
    top: 188px;
    color: var(--ink);
  }
  .name, .role {
    margin: 0;
    font-size: 45px;
    line-height: 56px;
    font-weight: 400;
  }
  .contact {
    margin: 6px 0 0;
    font-size: 24px;
    line-height: 32px;
  }
  .services {
    margin: 2px 0 0;
    font-size: 24px;
    line-height: 34px;
    color: var(--rose);
  }
</style>
</head>
<body>
  <section class="card">
    <div class="brand">
      <span class="brand-dot"></span>
      <span class="brand-name">Veltrin Lending</span>
    </div>
    <div class="details">
      <h1 class="name">Marnie Veltrin</h1>
      <h2 class="role">Finance Specialist</h2>
      <p class="contact">0438 215 962<br>marnie@veltrinlending.com.au</p>
      <p class="services">Residential / Commercial / Equipment</p>
    </div>
  </section>
</body>
</html>
```